A4 Flyer for charity car show

The "Bramble Ridge Charity Motor Fair" is an annual event that supports a different charity each year. The event aims to aim money and awareness for a cause as well as display a wide range of different cars that are in the community. These include classic cars, muscle cars, exotic cars and many more.

Information to be included:

The event will be held on: 15th of July 2018.
Charity Supported: Proudly supporting Kestrel Wings Australia
Location: Dorrit Oval, Wendaroo
Website: http://www.brambleridgemotorfair.com.au/

Target Market(s)

Car enthusiasts, professionals

Industry/Entity Type

Charity

Requirements
Must have
• Any car used in the flyer must look like they are in a field. Cars used must be right hand drive.

```html
<!DOCTYPE html>
<html lang="en">
<head>
<meta charset="utf-8">
<title>Bramble Ridge Charity Motor Fair – Flyer</title>
<link rel="stylesheet" href="https://fonts.googleapis.com/css2?family=Archivo+Black&family=Roboto:wght@300;400;700&display=swap">
<style>
  :root {
    --night: #150605;
    --ember: #c3120c;
    --orange: #f08a1e;
    --yellow: #f5e21c;
    --cream: #f7eccb;
    --gold: #c9a45a;
    --cocoa: #2b1712;
    --white: #ffffff;
    --navy: #1f3553;
    --ink: #333b47;
    --mist: #eef0f1;
    --car-blue: #3b63b8;
    --car-red: #d3261b;
    --car-black: #1b1b1b;
    --car-yellow: #e3ae1c;
  }
  * { margin: 0; padding: 0; box-sizing: border-box; }
  html, body { width: 927px; height: 1200px; overflow: hidden; background: var(--white); }
  .flyer {
    position: relative;
    width: 927px;
    height: 1200px;
    overflow: hidden;
    font-family: "Roboto", Arial, sans-serif;
    background: var(--white);
  }
  .hero-backdrop {
    position: absolute;
    left: 0; top: 0;
    width: 927px; height: 760px;
    background:
      radial-gradient(ellipse 560px 240px at 50% 380px, rgba(255,95,45,.8), rgba(240,48,26,.45) 45%, rgba(195,18,12,0) 75%),
      linear-gradient(to bottom, #1a0504 0, #4a0906 12%, var(--ember) 32%, #b80f0a 52%, #6a0b07 72%, #b9a8a6 86%, var(--white) 100%);
  }
  .info-panel {
    position: absolute;
    left: 83px; top: 490px;
    width: 761px; height: 335px;
    background: linear-gradient(to bottom, rgba(21,6,5,0) 0, rgba(21,6,5,.75) 22%, var(--night) 45%, var(--night) 100%);
  }
  .venue {
    position: absolute;
    top: 70px; left: 0; width: 100%;
    text-align: center;
    color: var(--white);
    font-weight: 700;
    font-size: 30px;
    line-height: 34px;
  }
  .title-line {
    position: absolute;
    left: 0; width: 100%;
    text-align: center;
    font-family: "Archivo Black", "Arial Black", sans-serif;
    line-height: 1;
    white-space: nowrap;
  }
  .title-name {
    top: 128px;
    font-size: 82px;
    color: var(--orange);
    letter-spacing: -1px;
  }
  .title-charity {
    top: 234px;
    font-size: 52px;
    color: var(--yellow);
    -webkit-text-stroke: 2px #3a2a08;
  }
  .title-motor {
    top: 306px;
    font-size: 160px;
    letter-spacing: -2px;
    background: linear-gradient(to bottom, #ffffff 0, var(--cream) 45%, var(--gold) 100%);
    -webkit-background-clip: text;
    background-clip: text;
    -webkit-text-fill-color: transparent;
    -webkit-text-stroke: 4px #5a2a0c;
    filter: drop-shadow(0 6px 0 #3a1208);
  }
  .title-fair {
    position: absolute;
    top: 480px; left: 560px;
    font-family: "Archivo Black", "Arial Black", sans-serif;
    font-size: 92px;
    line-height: 1;
    color: var(--cocoa);
    text-shadow: 4px 4px 0 var(--white), -4px -4px 0 var(--white), 4px -4px 0 var(--white), -4px 4px 0 var(--white), 0 5px 0 var(--white), 5px 0 0 var(--white);
    transform: rotate(-8deg);
    transform-origin: left bottom;
  }
  .event-date {
    position: absolute;
    top: 634px; left: 0; width: 100%;
    text-align: center;
    font-family: "Archivo Black", "Arial Black", sans-serif;
    font-size: 56px;
    line-height: 1;
    color: #2a1c0a;
    -webkit-text-stroke: 2.5px var(--yellow);
  }
  .event-date sup { font-size: 32px; vertical-align: 22px; }
  .date-glow {
    position: absolute;
    top: 700px; left: 213px;
    width: 500px; height: 4px;
    background: radial-gradient(ellipse at center, #fff2c0 0, var(--orange) 30%, rgba(240,138,30,0) 70%);
  }
  .intro {
    position: absolute;
    top: 726px; left: 130px;
    width: 668px;
    color: var(--white);
    font-size: 17px;
    line-height: 22px;
    text-align: justify;
    text-align-last: left;
  }
  .car-lineup {
    position: absolute;
    top: 812px; left: 34px;
    width: 852px; height: 142px;
    border-radius: 70px;
    background: linear-gradient(to right,
      var(--car-blue) 0, var(--car-blue) 16%,
      var(--car-red) 24%, var(--car-red) 38%,
      var(--car-black) 46%, var(--car-black) 58%,
      var(--car-yellow) 66%, var(--car-yellow) 80%,
      var(--car-red) 88%, var(--car-red) 100%);
    box-shadow: 0 10px 18px rgba(0,0,0,.25);
  }
  .footer-wave {
    position: absolute;
    left: 0; top: 985px;
    width: 927px; height: 215px;
  }
  .supporter-mark {
    position: absolute;
    top: 1060px; left: 58px;
    width: 130px;
    text-align: center;
    color: var(--ink);
    font-weight: 400;
    font-size: 20px;
    line-height: 24px;
  }
  .supporter-mark .dot {
    display: block;
    width: 14px; height: 14px;
    margin: 0 auto 6px;
    border-radius: 50%;
    background: var(--navy);
  }
  .supporter-note {
    position: absolute;
    top: 1048px; left: 190px;
    width: 318px;
    text-align: right;
    color: var(--ink);
    font-weight: 300;
    font-size: 14.5px;
    line-height: 20px;
  }
  .supporter-note .link {
    display: block;
    margin-top: 6px;
    font-weight: 700;
    font-size: 15px;
  }
  .show-mark {
    position: absolute;
    top: 1056px; left: 562px;
    display: flex;
    align-items: center;
    gap: 10px;
    color: var(--navy);
    font-weight: 400;
    font-size: 19px;
    line-height: 1;
  }
  .show-mark .dot {
    width: 34px; height: 34px;
    border-radius: 50%;
    background: var(--navy);
  }
  .show-site {
    position: absolute;
    top: 1110px; left: 534px;
    width: 360px;
    text-align: center;
    color: var(--navy);
    font-weight: 300;
    font-size: 21px;
  }
</style>
</head>
<body>
<main class="flyer">
  <div class="hero-backdrop" role="img" aria-label="Dark red background with glowing streaks of red light"></div>
  <div class="info-panel"></div>

  <p class="venue">Dorrit Oval Wendaroo</p>
  <h1>
    <span class="title-line title-name">BRAMBLE RIDGE</span>
    <span class="title-line title-charity">CHARITY</span>
    <span class="title-line title-motor">MOTOR</span>
    <span class="title-fair">Fair.</span>
  </h1>

  <p class="event-date">15<sup>TH</sup> OF JULY 2018</p>
  <div class="date-glow"></div>

  <p class="intro">The Bramble Ridge Charity Motor Fair is a community based event which attracts car lovers from all over NSW. Prizes are offered in a wide range of categories. A great family day out with the goal of the event to support a different charity each year.</p>

  <div class="car-lineup" role="img" aria-label="Photo of five cars in a row: a blue classic muscle car, a red exotic sports car, a black vintage sedan, a yellow muscle car and a red supercar"></div>

  <svg class="footer-wave" viewBox="0 0 927 215" aria-hidden="true">
    <path d="M0 40 Q 420 -10 927 60 L 927 215 L 0 215 Z" fill="var(--orange)"/>
    <path d="M0 44 Q 420 4 927 82 L 927 215 L 0 215 Z" fill="var(--white)"/>
    <path d="M0 150 Q 460 120 927 170 L 927 215 L 0 215 Z" fill="var(--mist)" opacity=".6"/>
  </svg>

  <div class="supporter-mark"><span class="dot"></span>Kestrel Wings</div>
  <p class="supporter-note">This year the Bramble Ridge Charity Motor Fair is extremely proud to be supporting the Kestrel Wings Australia.<span class="link">www.kestrelwings.org.au</span></p>

  <div class="show-mark"><span class="dot"></span>Bramble Ridge Motor Fair</div>
  <p class="show-site">www.brambleridgemotorfair.com.au</p>
</main>
</body>
</html>
```